PSD website for property company

Please read the brief thoroughly.

We are looking for a new website for a property group that does property acquisitions, property development and property management.
They buy, build and lease core inner city industrial assets in Sydney, Australia.
They also invest in residential developments.

Site menu
- Home page
- Property – sub menus include – Leasing ; Projects ; Investments ; Property Management
- Capital and finance
- About
- Contact

They like this website
https://www.velmorn.com.au/

They want the site to be clean, modern and bold.
They like few colors, even black and white is OK to submit

They have a logo and style guide and useable images here:
http://www.quorvex.net/temp/PellikWeb2019.zip
The zip file is also attached to this project.
We have supplied some images to give you an idea, but we will also require you to provide at least 3 extra images from stock photos.
Use your imagination.

I am expecting a lot of similar designs, so be aware the photos you choose will be really important.
They want really 3 good stock photos used and supplied without charge.
Please not too generic, I repeat the quality of the photos is important.
You may provide several photos (but not in multiple submissions please) and we will choose the best three to be provided.

The winner will be selected on a single home page design and required to provide;
All photos use in original format without charge
A second ‘standard page’ template design based on the winning home page design

```html
<!DOCTYPE html>
<html lang="en">
<head>
<meta charset="utf-8">
<title>Pellik Property Group</title>
<link href="https://fonts.googleapis.com/css2?family=Poppins:wght@400;500;600;700&family=Open+Sans:wght@400;600&display=swap" rel="stylesheet">
<style>
  :root{
    --green:#5f7b45;
    --green-dark:#4a6334;
    --green-pale:#dfe7d2;
    --ink:#1b1b1b;
    --grey:#6f6f6f;
    --light:#f2f2f2;
    --white:#ffffff;
    --black:#0c0c0c;
  }
  *{box-sizing:border-box;margin:0;padding:0}
  html,body{width:1200px;height:2592px;overflow:hidden}
  body{position:relative;background:var(--white);font-family:"Open Sans",sans-serif;color:var(--ink)}

  /* header */
  .site-header{position:absolute;top:0;left:0;width:1200px;height:60px;background:var(--white);z-index:5}
  .logo{position:absolute;left:40px;top:14px;font-family:"Poppins",sans-serif;font-weight:600;font-size:28px;letter-spacing:4px;color:var(--ink)}
  .main-nav{position:absolute;right:40px;top:22px;display:flex;gap:26px;font-family:"Poppins",sans-serif;font-size:11px;font-weight:500;letter-spacing:.5px;text-transform:uppercase}
  .main-nav span{color:var(--ink)}
  .dropdown{position:absolute;left:800px;top:62px;width:190px;background:var(--white);box-shadow:0 6px 18px rgba(0,0,0,.12);padding:14px 18px;z-index:6}
  .dropdown li{list-style:none;font-family:"Poppins",sans-serif;font-size:11px;text-transform:uppercase;color:var(--ink);padding:6px 0;border-bottom:1px solid #eee}
  .dropdown li:last-child{border-bottom:none}

  /* hero */
  .hero{position:absolute;top:60px;left:0;width:1200px;height:460px}
  .hero svg{position:absolute;inset:0}
  .hero-title{position:absolute;left:60px;top:92px;width:480px;text-align:center;font-family:"Poppins",sans-serif;font-weight:700;font-size:30px;line-height:1.2;color:var(--white);text-transform:uppercase}
  .btn-outline{position:absolute;left:200px;top:172px;width:200px;height:40px;border:2px solid var(--white);border-radius:20px;color:var(--white);font-family:"Poppins",sans-serif;font-size:13px;display:flex;align-items:center;justify-content:center;gap:8px}
  .scroll-label{position:absolute;left:78px;top:250px;writing-mode:vertical-rl;color:var(--white);font-family:"Poppins",sans-serif;font-size:11px;letter-spacing:4px;text-transform:uppercase}

  /* story */
  .story{position:absolute;top:560px;left:0;width:1200px;height:420px}
  .story-bg{position:absolute;left:0;top:160px;width:1200px;height:240px}
  .eyebrow{position:absolute;left:40px;top:50px;font-family:"Poppins",sans-serif;font-size:11px;letter-spacing:2px;color:var(--green);text-transform:uppercase}
  .story h2{position:absolute;left:40px;top:66px;font-family:"Poppins",sans-serif;font-weight:700;font-size:36px;color:var(--ink)}
  .story-text{position:absolute;left:40px;top:130px;width:520px;font-size:12.5px;line-height:1.75;color:var(--grey)}
  .story-text p+p{margin-top:16px}
  .story-photo{position:absolute;left:608px;top:48px;width:480px;height:332px;background:linear-gradient(160deg,#9aa3ab 0%,#5c6670 55%,#3a3f45 100%)}

  /* services grid */
  .services{position:absolute;top:1010px;left:0;width:1200px;height:592px;display:grid;grid-template-columns:repeat(3,400px);grid-template-rows:repeat(2,296px)}
  .tile{position:relative}
  .tile-label{position:absolute;left:28px;bottom:34px;color:var(--white);font-family:"Poppins",sans-serif;font-weight:600;font-size:18px}
  .tile-sub{position:absolute;left:28px;bottom:18px;color:rgba(255,255,255,.75);font-size:10px}
  .t1{background:linear-gradient(160deg,#3a3a3a,#1f1f1f)}
  .t2{background:linear-gradient(170deg,#cfd8de 0%,#a58a72 60%,#6c5646 100%)}
  .t3{background:linear-gradient(170deg,#dfe7ee 0%,#9b8d7c 60%,#5e5449 100%)}
  .t4{background:linear-gradient(170deg,#b9a48e 0%,#7a5e47 60%,#3f3128 100%)}
  .t5{background:linear-gradient(170deg,#c9d7e4 0%,#9b5e44 60%,#5c3828 100%)}
  .t6{background:linear-gradient(170deg,#d6e2ec 0%,#8f8f92 60%,#4d4f55 100%)}
  .tile-icon{position:absolute;left:188px;top:124px}

  /* newsletter */
  .newsletter{position:absolute;top:1640px;left:0;width:1200px;height:504px;overflow:hidden}
  .newsletter svg.band{position:absolute;inset:0}
  .news-photo{position:absolute;left:60px;top:40px;width:540px;height:464px;background:linear-gradient(180deg,#cdd6de 0%,#6f8fb0 40%,#33475e 75%,#1e2a36 100%)}
  .news-title{position:absolute;left:760px;top:44px;width:360px;text-align:center;font-family:"Poppins",sans-serif;font-weight:700;font-size:26px;color:var(--white);text-transform:uppercase}
  .news-sub{position:absolute;left:760px;top:88px;width:360px;text-align:center;font-size:11px;color:rgba(255,255,255,.85)}
  .news-form{position:absolute;left:780px;top:132px;width:320px}
  .field{height:34px;border:1.5px solid rgba(255,255,255,.8);border-radius:17px;margin-bottom:14px;padding:0 18px;display:flex;align-items:center;justify-content:space-between;font-size:10px;color:rgba(255,255,255,.85)}
  .btn-submit{position:absolute;left:870px;top:402px;width:140px;height:38px;border-radius:19px;background:var(--white);color:var(--ink);font-family:"Poppins",sans-serif;font-weight:600;font-size:12px;display:flex;align-items:center;justify-content:center}

  /* footer */
  .site-footer{position:absolute;top:2144px;left:0;width:1200px;height:448px;background:var(--black);color:var(--white);text-align:center}
  .footer-bg{position:absolute;top:0;height:448px}
  .footer-bg.left{left:0;width:300px}
  .footer-bg.right{right:0;width:380px}
  .footer-logo{position:absolute;left:0;width:1200px;top:48px;font-family:"Poppins",sans-serif;font-weight:600;font-size:24px;letter-spacing:4px}
  .footer-q{position:absolute;left:0;width:1200px;top:92px;font-family:"Poppins",sans-serif;font-size:22px}
  .footer-cta{position:absolute;left:0;width:1200px;top:122px;font-family:"Poppins",sans-serif;font-weight:700;font-size:30px;text-transform:uppercase}
  .footer-phone{position:absolute;left:0;width:1200px;top:184px;font-family:"Poppins",sans-serif;font-weight:600;font-size:26px}
  .footer-line{position:absolute;left:0;width:1200px;font-size:12px;color:rgba(255,255,255,.85)}
  .copyright{position:absolute;left:0;width:1200px;top:308px;font-size:8px;letter-spacing:1px;color:rgba(255,255,255,.6);text-transform:uppercase}
  .social{position:absolute;left:0;width:1200px;top:328px;display:flex;justify-content:center;gap:12px}
  .social span{width:10px;height:10px;border-radius:50%;background:rgba(255,255,255,.7)}
</style>
</head>
<body>

<header class="site-header">
  <div class="logo">PELLIK</div>
  <nav class="main-nav">
    <span>Home</span><span>Property ▾</span><span>Capital and finance</span><span>About</span><span>Contact</span>
  </nav>
</header>
<ul class="dropdown">
  <li>Leasing</li><li>Projects</li><li>Investments</li><li>Property management</li>
</ul>

<section class="hero">
  <svg width="1200" height="460" viewBox="0 0 1200 460">
    <defs>
      <linearGradient id="heroPhoto" x1="0" y1="0" x2="0" y2="1">
        <stop offset="0" stop-color="#c9d6e2"/>
        <stop offset=".45" stop-color="#4f6f96"/>
        <stop offset="1" stop-color="#1f2b3b"/>
      </linearGradient>
    </defs>
    <polygon points="760,0 1200,0 1200,300" fill="var(--green-pale)"/>
    <polygon points="0,0 760,0 470,460 0,460" fill="var(--green)"/>
    <polygon points="560,20 1080,20 1080,440 430,440" fill="url(#heroPhoto)" role="img" aria-label="Photo of a modern glass apartment building at dusk"/>
  </svg>
  <h1 class="hero-title">Let's take you to your dream house</h1>
  <div class="btn-outline">Explore our projects <span>→</span></div>
  <div class="scroll-label">Scroll</div>
</section>

<section class="story">
  <svg class="story-bg" role="img" aria-label="Faint line drawing of city buildings" viewBox="0 0 1200 240"><rect width="1200" height="240" fill="var(--light)" opacity=".6"/></svg>
  <div class="eyebrow">About</div>
  <h2>OUR STORY</h2>
  <div class="story-text">
    <p>We buy, build and lease core inner city industrial assets across Sydney. Our team brings together acquisition, development and management under one roof, giving every partner a clear path from first site visit to a fully leased building. We look for places with character and long term value, then shape them with care for the people who will work and live there.</p>
    <p>We also invest in residential developments, from boutique apartments to larger mixed use projects. Each one is planned with our partners and built to last, with a focus on quality design, sound finance and homes that stay in demand for years.</p>
  </div>
  <div class="story-photo" role="img" aria-label="Photo of a tall modern office tower"></div>
</section>

<section class="services">
  <div class="tile t1" role="img" aria-label="Photo of a dark brick industrial building">
    <svg class="tile-icon" width="24" height="24" viewBox="0 0 24 24"><path d="M4 6h8M4 6v14h14v-8M14 4h6v6M20 4l-9 9" stroke="#fff" stroke-width="2" fill="none"/></svg>
    <div class="tile-label">Leasing</div><div class="tile-sub">View more</div>
  </div>
  <div class="tile t2" role="img" aria-label="Photo of a luxury apartment building with arched windows">
    <div class="tile-label">Luxury Apartments</div><div class="tile-sub">View more</div>
  </div>
  <div class="tile t3" role="img" aria-label="Photo of a row of city buildings">
    <div class="tile-label">Property Management</div><div class="tile-sub">View more</div>
  </div>
  <div class="tile t4" role="img" aria-label="Photo of a modern hotel terrace">
    <div class="tile-label">Modern Hotels</div><div class="tile-sub">View more</div>
  </div>
  <div class="tile t5" role="img" aria-label="Photo of a red brick residential block">
    <div class="tile-label">Property Investment</div><div class="tile-sub">View more</div>
  </div>
  <div class="tile t6" role="img" aria-label="Photo of a contemporary apartment facade">
    <div class="tile-label">Buy</div><div class="tile-sub">View more</div>
  </div>
</section>

<section class="newsletter">
  <svg class="band" width="1200" height="504" viewBox="0 0 1200 504">
    <defs>
      <linearGradient id="newsBand" x1="0" y1="0" x2="1" y2="0">
        <stop offset="0" stop-color="var(--green-dark)"/>
        <stop offset="1" stop-color="var(--green)"/>
      </linearGradient>
    </defs>
    <rect width="1200" height="504" fill="url(#newsBand)"/>
    <polygon points="0,120 300,0 0,0" fill="var(--green-pale)"/>
  </svg>
  <div class="news-photo" role="img" aria-label="Photo of a glass apartment building lit at night"></div>
  <h2 class="news-title">Keep up to date</h2>
  <p class="news-sub">Sign up to hear about our latest projects and new opportunities.</p>
  <div class="news-form">
    <div class="field">Name</div>
    <div class="field">Last name</div>
    <div class="field">Email</div>
    <div class="field">Phone</div>
    <div class="field">Message <span>▾</span></div>
  </div>
  <div class="btn-submit">Submit</div>
</section>

<footer class="site-footer">
  <svg class="footer-bg left" role="img" aria-label="Faint architectural plan drawing" viewBox="0 0 300 448"><rect width="300" height="448" fill="#141414"/></svg>
  <svg class="footer-bg right" role="img" aria-label="Faint architectural plan drawing" viewBox="0 0 380 448"><rect width="380" height="448" fill="#161616"/></svg>
  <div class="footer-logo">PELLIK</div>
  <div class="footer-q">Have More Questions?</div>
  <div class="footer-cta">Contact us today!</div>
  <div class="footer-phone">+61 2 9876 5400</div>
  <div class="footer-line" style="top:234px">info@pellik.com</div>
  <div class="footer-line" style="top:258px">48 Harbour Lane, Sydney, Australia</div>
  <div class="copyright">Copyright © 2019 Pellik. All rights reserved.</div>
  <div class="social"><span></span><span></span><span></span><span></span></div>
</footer>

</body>
</html>
```